Certified Public Accountant specializing in tax preparation.

I need a business card designed that conveys knowledgeability, trustworthiness and competency. I am a licensed CPA and hold a Master's in taxation. As this is a personal service business, I would like to include my picture on the card.

```html
<!DOCTYPE html>
<html lang="en">
<head>
<meta charset="UTF-8">
<title>Clara Jane Holt – Business Card</title>
<link href="https://fonts.googleapis.com/css2?family=Delius&family=Lato:wght@400;700&display=swap" rel="stylesheet">
<style>
  :root {
    --backdrop: #2a2a2a;
    --card: #f4f3f2;
    --accent: #e8236f;
    --ink: #1e1e1e;
    --photo-dark: #5a4038;
    --photo-light: #e8c3d2;
  }
  * { margin: 0; padding: 0; box-sizing: border-box; }
  html, body {
    width: 1200px; height: 800px; overflow: hidden;
    background: var(--backdrop);
  }
  .canvas {
    position: relative; width: 1200px; height: 800px;
    display: flex; align-items: center; justify-content: center;
  }
  .business-card {
    position: relative; width: 1050px; height: 600px;
    background: var(--card); border-radius: 40px; overflow: hidden;
    font-family: 'Lato', sans-serif; color: var(--ink);
  }
  .accent-bar {
    position: absolute; left: 36px; width: 9px; background: var(--accent);
  }
  .accent-bar--name { top: 150px; height: 92px; }
  .accent-bar--contact { top: 345px; height: 215px; }
  .identity { position: absolute; left: 78px; top: 138px; }
  .identity__name {
    font-family: 'Delius', cursive; font-size: 52px; color: var(--accent);
    line-height: 1.1; font-weight: 400;
  }
  .identity__credentials { font-size: 23px; margin-top: 4px; letter-spacing: 0.3px; }
  .identity__divider { margin: 0 10px; }
  .address {
    position: absolute; left: 110px; top: 318px;
    font-size: 24px; line-height: 1.4; font-style: normal;
  }
  .contact-list {
    position: absolute; left: 120px; top: 415px; list-style: none;
  }
  .contact-list__item {
    display: flex; align-items: center; gap: 16px; font-size: 24px; height: 50px;
  }
  .contact-list__icon { width: 30px; height: 30px; flex: none; }
  .portrait {
    position: absolute; right: 30px; top: 80px; bottom: 0; width: 410px;
    background: linear-gradient(180deg, var(--photo-dark) 0%, var(--photo-light) 100%);
  }
</style>
</head>
<body>
<main class="canvas">
  <article class="business-card">
    <span class="accent-bar accent-bar--name"></span>
    <span class="accent-bar accent-bar--contact"></span>

    <header class="identity">
      <h1 class="identity__name">Clara Jane Holt</h1>
      <p class="identity__credentials">Licensed CPA<span class="identity__divider">|</span>Master's in taxation</p>
    </header>

    <address class="address">
      48 Elm Row, Suite B, London<br>UK B0034C
    </address>

    <ul class="contact-list">
      <li class="contact-list__item">
        <svg class="contact-list__icon" viewBox="0 0 30 30" aria-hidden="true">
          <circle cx="15" cy="15" r="15" fill="var(--accent)"/>
          <path d="M10 8c1-1 2-1 3 0l1.5 2.5c.5 1 0 1.7-.7 2.3-.5.4-.4 1 .3 2l1.6 1.8c.8.8 1.4.9 1.9.4.7-.7 1.4-1.2 2.3-.6l2.4 1.6c.9.7.8 1.7 0 2.7-1.2 1.4-3 1.8-5.5.3-2.6-1.6-5.2-4.3-6.7-7-1.3-2.4-1.1-4.5-.1-6z" fill="#fff"/>
        </svg>
        <span>010 482 3195</span>
      </li>
      <li class="contact-list__item">
        <svg class="contact-list__icon" viewBox="0 0 30 30" aria-hidden="true">
          <circle cx="15" cy="15" r="15" fill="var(--accent)"/>
          <rect x="8" y="10" width="14" height="10" rx="1" fill="#fff"/>
          <path d="M8.5 10.5 15 16l6.5-5.5" fill="none" stroke="var(--accent)" stroke-width="1.4"/>
        </svg>
        <span>clara.holt@mailbox.com</span>
      </li>
      <li class="contact-list__item">
        <svg class="contact-list__icon" viewBox="0 0 30 30" aria-hidden="true">
          <circle cx="15" cy="15" r="15" fill="var(--accent)"/>
          <g fill="none" stroke="#fff" stroke-width="1.4">
            <circle cx="15" cy="15" r="7.5"/>
            <ellipse cx="15" cy="15" rx="3.2" ry="7.5"/>
            <path d="M7.5 15h15M9 11h12M9 19h12"/>
          </g>
        </svg>
        <span>www.clarajaneholt.com</span>
      </li>
    </ul>

    <div class="portrait" role="img" aria-label="Portrait photo of the accountant"></div>
  </article>
</main>
</body>
</html>
```